New startup requiring business card

New company needed a business card / logo. Company name is
Minthel
Company is providing IT software sales, partnering and consulting services across the APAC region. Catch line is "growing together".
We currently have a feeling yellow as the primary colour given its meaning across the region but open to ideas. Main brief is we want something smart, clean and professional while still leveraging the strength of the name.
A major part of the business is mutually beneficial partnerships, not sure if this helps but maybe visual around linkages between objects.
Also wanting a standard size card, preference is something that will have a D/S cello sheen finish in a matt. But again open to ideas, wow us!
Software

```html
<!DOCTYPE html>
<html lang="en">
<head>
<meta charset="utf-8">
<title>Minthel – Business Card</title>
<link href="https://fonts.googleapis.com/css2?family=Roboto+Condensed:wght@300;400;700&display=swap" rel="stylesheet">
<style>
  :root {
    --bg: #1f1f1f;
    --card-dark: #151515;
    --yellow: #e9dc1f;
    --yellow-deep: #c9b818;
    --ink: #1a1a1a;
    --light: #e6e6e6;
    --muted: #8a8a8a;
  }
  * { margin: 0; padding: 0; box-sizing: border-box; }
  html, body { width: 1200px; height: 1200px; overflow: hidden; }
  body {
    background: var(--bg);
    font-family: "Roboto Condensed", "Arial Narrow", sans-serif;
    position: relative;
  }
  .brand-lockup {
    position: absolute; left: 70px; top: 50px;
    display: flex; align-items: center; gap: 16px;
  }
  .brand-mark { width: 62px; height: 62px; border-radius: 50%; background: var(--light); }
  .brand-name { color: var(--light); font-weight: 700; font-size: 46px; line-height: 1; letter-spacing: 0.5px; }

  .card {
    position: absolute; left: 200px; width: 800px; height: 457px;
    box-shadow: 0 10px 28px rgba(0,0,0,0.55);
    overflow: hidden;
  }
  .card-front {
    top: 150px;
    background: linear-gradient(145deg, var(--yellow-deep) 0%, var(--yellow) 55%, #f5ea2a 100%);
    display: flex; flex-direction: column; align-items: center; justify-content: center;
  }
  .front-lockup { display: flex; align-items: center; gap: 12px; }
  .front-mark { width: 66px; height: 66px; border-radius: 50%; background: var(--ink); }
  .front-name { color: var(--ink); font-weight: 700; font-size: 44px; line-height: 1; }
  .front-web { color: #3a3612; font-size: 19px; letter-spacing: 4px; margin-top: 12px; }

  .card-back { top: 680px; background: var(--card-dark); }
  .back-lockup {
    position: absolute; right: 30px; top: 26px;
    display: flex; align-items: center; gap: 8px;
  }
  .back-mark { width: 46px; height: 46px; border-radius: 50%; background: var(--light); }
  .back-name { color: var(--light); font-weight: 700; font-size: 28px; line-height: 1; }

  .accent-square { position: absolute; left: 0; top: 221px; width: 81px; height: 56px; background: var(--yellow); }
  .accent-bar { position: absolute; left: 454px; top: 300px; width: 343px; height: 56px; background: var(--yellow); }

  .person { position: absolute; left: 100px; top: 218px; }
  .person-name { font-size: 37px; font-weight: 400; line-height: 1; color: var(--light); }
  .person-name .first { color: var(--yellow); }
  .person-title { color: var(--muted); font-size: 18px; font-weight: 300; margin-top: 4px; letter-spacing: 0.3px; }

  .contact { position: absolute; left: 100px; top: 305px; font-size: 12.5px; line-height: 19px; color: var(--muted); font-weight: 300; }
  .contact .phone { color: var(--light); font-weight: 400; }
</style>
</head>
<body>
  <header class="brand-lockup">
    <div class="brand-mark"></div>
    <div class="brand-name">MINTHEL</div>
  </header>

  <section class="card card-front">
    <div class="front-lockup">
      <div class="front-mark"></div>
      <div class="front-name">MINTHEL</div>
    </div>
    <div class="front-web">WWW.MINTHEL.EXAMPLE</div>
  </section>

  <section class="card card-back">
    <div class="back-lockup">
      <div class="back-mark"></div>
      <div class="back-name">MINTHEL</div>
    </div>

    <div class="accent-square"></div>
    <div class="person">
      <div class="person-name"><span class="first">Daniel</span> Marsh</div>
      <div class="person-title">EXECUTIVE CREATIVE DIRECTOR</div>
    </div>

    <div class="contact">
      <div>LORN STREET 12 BLOCK C, HARBOUR CITY - AVALON</div>
      <div class="phone">T. +000 4127 580 &nbsp;+000 316 9042</div>
      <div>E. DANIEL@MINTHELMAIL.COM | WWW.MINTHEL.EXAMPLE</div>
    </div>

    <div class="accent-bar"></div>
  </section>
</body>
</html>
```